business cards for heating company

I need business cards for my heating air conditioning and chimney company located in upstate NY I would like for them to be colorful and catchy on heavy stock with preferably a glossy finish on front of card but the ability to write something on one half of the back with maybe some bullets on the other half of the back I also need to be able to change the name and title of employees on the card and also incorporate some of our current look and feel from our trucks and website I also want to be able to use this design or similar to have door hangers made lawn signs coffee mugs key chains etc. our website is Brindlecove.com

Target Market(s)

homeowners

Industry/Entity Type

Air Conditioning

Contact Information for Business Card

should have website brindlecove.com , phone number 585-437-9168 please look at website for ideas

Font styles to use
Sans Serif

Colors
ec1f27
3176b5
fbee3f

Requirements
Must have
• a complete look
Nice to have
• a discount offer like 10% military and first responders
• senior discount %5

```html
<!DOCTYPE html>
<html lang="en">
<head>
<meta charset="utf-8">
<title>Brindle Cove – Business Card</title>
<link rel="stylesheet" href="https://fonts.googleapis.com/css2?family=Jost:wght@300;400&family=Nunito:wght@900&family=Arimo&display=swap">
<style>
  :root {
    --magenta-deep: #c4176a;
    --magenta-light: #e6357f;
    --brand-red: #ec1f27;
    --brand-blue: #3176b5;
    --brand-yellow: #fbee3f;
    --white: #ffffff;
    --page: #ffffff;
  }
  * { margin: 0; padding: 0; box-sizing: border-box; }
  html, body {
    width: 1200px; height: 900px; overflow: hidden;
    background: var(--page);
  }
  .canvas { position: relative; width: 1200px; height: 900px; }

  .card {
    position: absolute;
    left: 320px; width: 562px; height: 324px;
    overflow: hidden;
    box-shadow: 0 10px 14px -8px rgba(0,0,0,0.12);
  }
  .card--front {
    top: 82px;
    background: linear-gradient(90deg, var(--magenta-deep) 0%, var(--magenta-deep) 12%, var(--magenta-light) 62%);
  }
  .card--back {
    top: 467px;
    background: radial-gradient(ellipse 340px 260px at 230px 180px, var(--magenta-light) 0%, var(--magenta-deep) 100%);
  }
  .card__pattern { position: absolute; top: 0; left: 0; width: 562px; height: 324px; }

  .brand {
    position: absolute; left: 8px; top: 14px;
    font-family: "Nunito", sans-serif; font-weight: 900;
    font-size: 39px; letter-spacing: 0.5px;
    color: var(--white); text-transform: uppercase;
    white-space: nowrap;
  }
  .brand__tagline {
    position: absolute; left: 38px; top: 64px;
    font-family: "Jost", sans-serif; font-weight: 400;
    font-size: 15px; letter-spacing: 0.6px;
    color: var(--white); white-space: nowrap;
  }

  .person { position: absolute; left: 264px; top: 68px; color: var(--white); font-family: "Jost", sans-serif; }
  .person__name { font-weight: 300; font-size: 33px; line-height: 1; letter-spacing: 0.6px; }
  .person__title { font-weight: 400; font-size: 12px; margin: 3px 0 0 4px; letter-spacing: 0.2px; }

  .contact { position: absolute; left: 260px; top: 142px; list-style: none; }
  .contact__item {
    position: relative; height: 52px;
    font-family: "Arimo", sans-serif; font-size: 17px; color: var(--white);
  }
  .contact__item:nth-child(3) { height: 56px; }
  .contact__icon { position: absolute; left: 0; top: 0; width: 28px; height: 28px; }
  .contact__text { position: absolute; left: 85px; top: 4px; white-space: nowrap; }
  .contact__text--phone { left: 90px; }
</style>
</head>
<body>
<main class="canvas">

  <section class="card card--front" aria-label="Card front">
    <svg class="card__pattern" viewBox="0 0 562 324" aria-hidden="false">
      <defs>
        <linearGradient id="patternToneFront" x1="0" y1="0" x2="1" y2="1">
          <stop offset="0" stop-color="#3176b5"/>
          <stop offset="0.35" stop-color="#ec1f27"/>
          <stop offset="0.6" stop-color="#fbee3f"/>
          <stop offset="1" stop-color="#ec1f27"/>
        </linearGradient>
      </defs>
      <polygon role="img" aria-label="Mosaic of red, blue and yellow triangles"
               points="370,0 562,0 562,324 370,324 269,161" fill="url(#patternToneFront)"/>
      <polyline points="370,0 269,161 370,324" fill="none" stroke="#ffffff" stroke-width="2"/>
    </svg>
    <h1 class="brand">Brindle Cove</h1>
    <p class="brand__tagline">HEATING, COOLING &amp; CHIMNEY</p>
  </section>

  <section class="card card--back" aria-label="Card back">
    <svg class="card__pattern" viewBox="0 0 562 324">
      <defs>
        <linearGradient id="patternToneBack" x1="0" y1="0" x2="1" y2="1">
          <stop offset="0" stop-color="#ec1f27"/>
          <stop offset="0.35" stop-color="#3176b5"/>
          <stop offset="0.65" stop-color="#fbee3f"/>
          <stop offset="1" stop-color="#3176b5"/>
        </linearGradient>
      </defs>
      <polygon role="img" aria-label="Mosaic of red, blue and yellow triangles"
               points="0,0 200,0 100,161 200,324 0,324" fill="url(#patternToneBack)"/>
      <polyline points="200,0 100,161 200,324" fill="none" stroke="#ffffff" stroke-width="2"/>
    </svg>

    <div class="person">
      <h2 class="person__name">YOUR NAME</h2>
      <p class="person__title">YOUR TITLE</p>
    </div>

    <ul class="contact">
      <li class="contact__item">
        <svg class="contact__icon" viewBox="0 0 28 28" aria-hidden="true">
          <path fill="#fff" d="M6 3 l4 -1 l3 6 l-3 2 c1 3 4 6 7 7 l2 -3 l6 3 l-1 4 c-1 2 -3 3 -5 2 C11 21 6 16 3 8 c-1 -2 1 -4 3 -5 z"/>
        </svg>
        <span class="contact__text contact__text--phone">124 456 7892</span>
      </li>
      <li class="contact__item">
        <svg class="contact__icon" viewBox="0 0 28 28" aria-hidden="true">
          <rect x="1" y="5" width="26" height="18" rx="2" fill="#fff"/>
          <polyline points="2,7 14,16 26,7" fill="none" stroke="#d42672" stroke-width="2"/>
        </svg>
        <span class="contact__text">Contact@example.com</span>
      </li>
      <li class="contact__item">
        <svg class="contact__icon" viewBox="0 0 28 28" aria-hidden="true" fill="none" stroke="#fff" stroke-width="1.6">
          <circle cx="14" cy="14" r="12.5"/>
          <ellipse cx="14" cy="14" rx="5.5" ry="12.5"/>
          <line x1="14" y1="1.5" x2="14" y2="26.5"/>
          <line x1="1.5" y1="14" x2="26.5" y2="14"/>
          <line x1="4" y1="7.5" x2="24" y2="7.5"/>
          <line x1="4" y1="20.5" x2="24" y2="20.5"/>
        </svg>
        <span class="contact__text">www.yourwebsite.com</span>
      </li>
    </ul>
  </section>

</main>
</body>
</html>
```